Verostel business card

Business card for sustainable investment company called "Verostel". Verostel is an exchange platform selling carbon credits between buyers and sellers. Carbon Credits are an environmental commodity for reducing global carbon emissions.

the card should obviously have our logo and the theme should be sustainability/environment mixed with a trading platform.

Contact Information for Business Card

Logo, Name, Title, Phone, Email

Colors
0054AA
0677BA
7BADD7
CADEEF
E8F1F8
0094D4
00A9DD
6FCCEA
C7EBF8
E9F6FB
00AB8E
00BBA5
67D7C9
C6EFE9
E9F9F6
59FF00
82FF00
B8FF75
E3FFCB
F4FFEA

```html
<!DOCTYPE html>
<html lang="en">
<head>
<meta charset="utf-8">
<title>Verostel business card</title>
<link href="https://fonts.googleapis.com/css2?family=Poppins:ital,wght@0,500;0,600;0,700;1,500&display=swap" rel="stylesheet">
<style>
  :root {
    --backdrop: #dddddd;
    --aqua: #36eaee;
    --sky: #2ecbee;
    --azure: #1f82ea;
    --ocean: #2596ec;
    --icon-fill: #36d9e8;
    --white: #ffffff;
    --shadow: rgba(0, 0, 0, 0.35);
  }
  html, body {
    margin: 0;
    padding: 0;
    width: 1200px;
    height: 1200px;
    overflow: hidden;
    background: var(--backdrop);
    font-family: "Poppins", sans-serif;
  }
  .card {
    position: absolute;
    left: 130px;
    width: 908px;
    height: 519px;
    box-shadow: 18px 18px 22px var(--shadow);
    color: var(--white);
    overflow: hidden;
  }
  .card--front {
    top: 64px;
    background: linear-gradient(90deg, var(--aqua) 0%, var(--sky) 35%, var(--azure) 100%);
    display: flex;
    align-items: center;
    justify-content: center;
    gap: 34px;
  }
  .card--back {
    top: 617px;
    background: linear-gradient(90deg, var(--ocean) 0%, var(--sky) 55%, var(--aqua) 100%);
  }
  .brand-dot {
    width: 110px;
    height: 110px;
    border-radius: 50%;
    background: var(--white);
  }
  .brand-name {
    font-weight: 600;
    font-size: 92px;
    letter-spacing: 2px;
    line-height: 1;
    margin-top: 8px;
  }
  .person-name {
    position: absolute;
    left: 61px;
    top: 80px;
    margin: 0;
    font-weight: 700;
    font-size: 55px;
    line-height: 1.1;
    letter-spacing: -0.5px;
  }
  .person-title {
    position: absolute;
    left: 61px;
    top: 137px;
    margin: 0;
    font-weight: 500;
    font-style: italic;
    font-size: 23px;
  }
  .contacts {
    position: absolute;
    left: 50px;
    top: 243px;
    margin: 0;
    padding: 0;
    list-style: none;
  }
  .contact {
    display: flex;
    align-items: center;
    height: 40px;
    margin-bottom: 9.5px;
    font-weight: 500;
    font-size: 27px;
  }
  .contact-icon {
    width: 36px;
    height: 36px;
    border: 2px solid var(--white);
    border-radius: 50%;
    background: var(--icon-fill);
    display: flex;
    align-items: center;
    justify-content: center;
    margin-right: 20px;
    flex-shrink: 0;
  }
  .contact-icon svg { width: 22px; height: 22px; }
</style>
</head>
<body>
  <section class="card card--front">
    <span class="brand-dot"></span>
    <span class="brand-name">VEROSTEL</span>
  </section>

  <section class="card card--back">
    <h1 class="person-name">NAME OF PERSON</h1>
    <p class="person-title">POSITION</p>
    <ul class="contacts">
      <li class="contact">
        <span class="contact-icon">
          <svg viewBox="0 0 24 24" fill="none" stroke="#fff" stroke-width="2.4" stroke-linecap="round">
            <path d="M9 5 C13 6 14 10 13 13 C12 16 10 18 8 19"/>
            <path d="M8 4.5 L10 5.5"/><path d="M7 18.5 L9 19.5"/>
          </svg>
        </span>Contact number
      </li>
      <li class="contact">
        <span class="contact-icon">
          <svg viewBox="0 0 24 24" fill="none" stroke="#fff" stroke-width="1.6">
            <path d="M12 22 L6.5 12 A6 6 0 1 1 17.5 12 Z"/>
            <circle cx="12" cy="9" r="2.2"/>
          </svg>
        </span>Address
      </li>
      <li class="contact">
        <span class="contact-icon">
          <svg viewBox="0 0 24 24" fill="none" stroke="#fff" stroke-width="1.8" stroke-linecap="round">
            <circle cx="12" cy="12" r="3.5"/>
            <path d="M15.5 9 V13.5 A2.3 2.3 0 0 0 20 13 V12 A8 8 0 1 0 16 19"/>
          </svg>
        </span>Email Address
      </li>
      <li class="contact">
        <span class="contact-icon">
          <svg viewBox="0 0 24 24" fill="none" stroke="#fff" stroke-width="1.4">
            <circle cx="12" cy="12" r="9"/>
            <ellipse cx="12" cy="12" rx="4" ry="9"/>
            <path d="M3 12 H21 M4.5 7.5 H19.5 M4.5 16.5 H19.5 M12 3 V21"/>
          </svg>
        </span>Website
      </li>
    </ul>
  </section>
</body>
</html>
```